A4 Tri-fold Brochure for Sedation Dentist Specialist Dr. Marlon and Sedation Dentistry.

I would like to create an A4 tri-fold brochure for our Dental Sedation Specialist Dr. Marlon Quade. Please carefully select the most suitable highlights from his bio below.

This brochure has two parts. Highlighting what makes Dr. Marlon Quade unique and trustworthy. Include a picture of him (attached). The second part is about sedation dentistry. All you need to know here: http://www.calmchairhub.example/what-is-calm-chair-treatment

Avoid making it too wordy.

Meet Dr. Rowan Elke Marlon Quade, DDS

Inspired to Become a Dentist:
As a child, Dr. Marlon Quade always felt stressed whenever he had to see a dentist. He knew that he wanted to become a dentist to help put patients completely at ease while they experienced quality dental care.

He is passionate about giving patients the healthy, beautiful smiles they deserve. “I find it fulfilling when I can see my patients’ beautiful smiles and how they can finally appreciate the joy of eating with a healthy set of teeth. However, what I love most about my job is the ability to provide a stress-free and comfortable experience at the dentist’s office, particularly for children, through sedation and general anesthesia.”

Educational Achievements:
Before becoming a dentist, Dr. Marlon Quade earned his undergraduate degree at the University of Northern Albury where he received a Bachelor of Medical Science Honor Specialization degree with distinction in biochemistry. He then completed his Doctor of Dental Surgery degree with honors at the University of Kestrelford. While there, he received the Linus Brandt Medal in his class for outstanding achievement in anesthesia. He then pursued his three-year residency as well as a master’s degree in dental anesthesia at the University of Kestrelford.

So he can provide his patients with the latest in dentistry, Dr. Marlon Quade enjoys pursuing additional knowledge, particularly in the areas of dental anesthesia as well as advanced technologies in dentistry. He is currently part of the Molar Horizons study club and has enrolled in the Core Anchor Short- Training Course. He also serves as a clinical instructor at the Pellvar Clinic at the University of Kestrelford.

Association Memberships:
In addition to his academic credentials, Dr. Marlon Quade is a member of several associations:
The Grand Guild of Oral Practitioners of Varnland (GGOPV)
Dental Continental Union of Dental Sedation (CUDS)
Northern Institute of Dental Sedation (NIDS)
Varnland Dental Council (VDC)
Outside the Practice

When he’s not at the practice, Dr. Marlon Quade enjoys spending time with his wife Greta and their two poodles Pippin and Pepper, who are spoiled rotten! “Greta and I love taking our dogs out on hikes and to the dog park on weekends. I also enjoy a wide range of activities from model building and playing the piano to soccer, gym and archery.” He stays fit by working out at the local Brightstride gym, and he likes to walk in Fernhollow Lake Park and Ashcombe Meadow Park.

Dr. Marlon Quade considers himself to be a kid at heart. He is a big fan of superheroes and animated movies. “I get really excited about any upcoming superhero or Lumawell Studioz movies. Till this day, I still collect superhero toy figures.”

He supports the TinyHearts Trust as well as the Varnland League for the Protection of Companion Creatures (LPCC).

Experience outstanding dental care with our highly skilled dentist. Contact us today to schedule an appointment with Dr. Marlon Quade! He speaks English, Cantonese, and Mandarin.

Target Market(s)

Mothers with young kids.

Industry/Entity Type

Dental

Font styles to use
Sans Serif

Requirements
Should not have
• Prices

```html
<!DOCTYPE html>
<html lang="en">
<head>
<meta charset="utf-8">
<title>Sleep Dentistry – Tri-fold Brochure</title>
<link href="https://fonts.googleapis.com/css2?family=Jost:wght@400;500;600;700&display=swap" rel="stylesheet">
<style>
  :root {
    --page-bg: #e9ecef;
    --paper: #ffffff;
    --brand-blue: #2aa3dc;
    --heading-blue: #1f6fb5;
    --brand-green: #5fd39a;
    --ink: #2d2d2d;
    --ink-soft: #4a4a4a;
    --photo-cool: #c9d3dc;
    --photo-warm: #b9a99a;
  }
  * { box-sizing: border-box; margin: 0; padding: 0; }
  html, body { width: 1200px; height: 800px; overflow: hidden; }
  body {
    background: var(--page-bg);
    font-family: "Jost", sans-serif;
    color: var(--ink);
  }
  .brochure {
    position: absolute;
    left: 30px; top: 20px;
    width: 1140px; height: 760px;
    display: flex;
    background: var(--paper);
    box-shadow: 0 6px 24px rgba(0,0,0,.15);
  }
  .panel {
    position: relative;
    width: 380px; height: 760px;
    overflow: hidden;
    background: var(--paper);
  }
  .panel + .panel { border-left: 1px solid #e2e5e8; }
  .panel-art { position: absolute; inset: 0; width: 380px; height: 760px; }

  /* Panel 1 – memberships */
  .memberships-title {
    position: absolute; left: 36px; top: 62px;
    font-size: 27px; font-weight: 500; color: var(--heading-blue);
  }
  .memberships-intro {
    position: absolute; left: 36px; top: 108px; width: 300px;
    font-size: 12.5px; line-height: 1.35; color: var(--ink);
  }
  .membership-list {
    position: absolute; left: 36px; top: 158px; width: 310px;
    list-style: none;
  }
  .membership-list li {
    position: relative;
    padding-left: 28px; margin-bottom: 16px;
    font-size: 15.5px; line-height: 1.2; color: var(--heading-blue);
  }
  .membership-list svg { position: absolute; left: 0; top: 5px; }
  .phone-line {
    position: absolute; left: 36px; bottom: 44px;
    display: flex; align-items: center; gap: 12px;
    font-size: 33px; font-weight: 600; color: #fff; letter-spacing: .5px;
  }

  /* Panel 2 – story */
  .story-title {
    position: absolute; left: 0; top: 52px; width: 380px;
    text-align: center;
    font-size: 26px; line-height: 1.2; font-weight: 500; color: var(--heading-blue);
  }
  .story-body {
    position: absolute; left: 40px; top: 140px; width: 300px;
    text-align: center; font-size: 13px; line-height: 1.4; color: var(--ink);
  }
  .story-body p + p { margin-top: 14px; }
  .story-divider {
    position: absolute; left: 70px; top: 498px; width: 240px;
    height: 1.5px; background: var(--brand-green);
  }
  .more-info {
    position: absolute; left: 0; top: 514px; width: 380px; text-align: center;
  }
  .more-info-label {
    font-size: 15px; font-weight: 500; color: var(--heading-blue); letter-spacing: .8px;
  }
  .more-info-url {
    margin-top: 6px; font-size: 14px; line-height: 1.35; color: var(--ink);
  }
  .web-line {
    position: absolute; left: 0; bottom: 40px; width: 380px;
    display: flex; justify-content: center; align-items: center; gap: 8px;
    font-size: 15px; color: #fff; letter-spacing: .3px;
  }

  /* Panel 3 – cover */
  .cover-title {
    position: absolute; left: 40px; top: 34px;
    font-size: 30px; font-weight: 500; color: var(--heading-blue);
  }
  .cover-title .accent { color: var(--brand-green); font-weight: 600; }
  .meet-block {
    position: absolute; right: 30px; bottom: 56px; text-align: right; color: #fff;
  }
  .meet-word { font-size: 42px; font-weight: 700; line-height: 1; letter-spacing: 1px; }
  .meet-name { margin-top: 8px; font-size: 15px; font-weight: 600; letter-spacing: .6px; }
</style>
</head>
<body>
<main class="brochure">

  <!-- Inside left panel -->
  <section class="panel panel-memberships">
    <svg class="panel-art" viewBox="0 0 380 760" aria-hidden="true">
      <path d="M0,650 Q180,560 380,520 L380,760 L0,760Z" fill="var(--brand-blue)"/>
      <path d="M0,628 Q180,538 380,496" fill="none" stroke="var(--brand-green)" stroke-width="12"/>
    </svg>
    <h2 class="memberships-title">Association Memberships</h2>
    <p class="memberships-intro">In addition to his academic credentials, Dr. Marlon Quade is a member of several associations:</p>
    <ul class="membership-list">
      <li><svg width="14" height="12" viewBox="0 0 14 12"><path d="M1,6 L5,10 L13,1" fill="none" stroke="#2d2d2d" stroke-width="2"/></svg>The Grand Guild of Oral Practitioners of Varnland (GGOPV)</li>
      <li><svg width="14" height="12" viewBox="0 0 14 12"><path d="M1,6 L5,10 L13,1" fill="none" stroke="#2d2d2d" stroke-width="2"/></svg>Dental Continental Union of Dental Sedation (CUDS)</li>
      <li><svg width="14" height="12" viewBox="0 0 14 12"><path d="M1,6 L5,10 L13,1" fill="none" stroke="#2d2d2d" stroke-width="2"/></svg>Northern Institute of Dental Sedation (NIDS)</li>
      <li><svg width="14" height="12" viewBox="0 0 14 12"><path d="M1,6 L5,10 L13,1" fill="none" stroke="#2d2d2d" stroke-width="2"/></svg>Varnland Dental Council (VDC)</li>
    </ul>
    <svg class="panel-art" viewBox="0 0 380 760">
      <defs>
        <linearGradient id="exam-photo" x1="0" y1="0" x2="1" y2="1">
          <stop offset="0" stop-color="#e6ebef"/>
          <stop offset=".6" stop-color="#c8d6e2"/>
          <stop offset="1" stop-color="#3f6fc0"/>
        </linearGradient>
      </defs>
      <circle cx="160" cy="560" r="128" fill="var(--brand-green)"/>
      <circle cx="160" cy="560" r="119" fill="url(#exam-photo)" role="img" aria-label="Photo of a dentist in a mask examining a smiling young patient in the chair"/>
    </svg>
    <div class="phone-line">
      <svg width="30" height="30" viewBox="0 0 30 30" aria-hidden="true">
        <circle cx="15" cy="15" r="13" fill="none" stroke="#fff" stroke-width="2.5"/>
        <path d="M10,8 L13,8 L14,12 L12,13.5 Q14,17 17,18.5 L18.5,16.5 L22,17.5 L22,20.5 Q14,21 9,12 Z" fill="#fff"/>
      </svg>
      <span>800-555-0199</span>
    </div>
  </section>

  <!-- Inside middle panel -->
  <section class="panel panel-story">
    <svg class="panel-art" viewBox="0 0 380 760">
      <defs>
        <linearGradient id="smile-photo" x1="0" y1="0" x2="1" y2="1">
          <stop offset="0" stop-color="#f1f1f1"/>
          <stop offset=".5" stop-color="#e3e3e3"/>
          <stop offset="1" stop-color="#f5f5f5"/>
        </linearGradient>
      </defs>
      <rect x="0" y="0" width="380" height="660" fill="url(#smile-photo)" role="img" aria-label="Faint background photo of a smiling woman"/>
      <path d="M0,640 Q190,690 380,610 L380,760 L0,760Z" fill="var(--brand-blue)"/>
      <path d="M0,628 Q190,676 380,596" fill="none" stroke="var(--brand-green)" stroke-width="12"/>
      <path d="M0,640 Q190,690 380,610" fill="none" stroke="#fff" stroke-width="6"/>
    </svg>
    <h2 class="story-title">Inspired to<br>Become a Dentist</h2>
    <div class="story-body">
      <p>As a child, Dr. Marlon Quade always felt stressed whenever he had to see a dentist. He knew that he wanted to become a dentist to help put patients completely at ease while they experienced quality dental care.</p>
      <p>He is passionate about giving patients the healthy, beautiful smiles they deserve. “I find it fulfilling when I can see my patients’ beautiful smiles and how they can finally appreciate the joy of eating with a healthy set of teeth. However, what I love most about my job is the ability to provide a stress-free and comfortable experience at the dentist’s office, particularly for children, through sedation and general anesthesia.”</p>
    </div>
    <div class="story-divider"></div>
    <div class="more-info">
      <p class="more-info-label">ALL YOU NEED TO KNOW HERE:</p>
      <p class="more-info-url">http://www.calmchairhub.example<br>/what-is-calm-chair-treatment</p>
    </div>
    <div class="web-line">
      <svg width="14" height="14" viewBox="0 0 14 14" aria-hidden="true">
        <circle cx="7" cy="7" r="6" fill="none" stroke="#fff" stroke-width="1.3"/>
        <ellipse cx="7" cy="7" rx="2.6" ry="6" fill="none" stroke="#fff" stroke-width="1.1"/>
        <path d="M1,7 H13" stroke="#fff" stroke-width="1.1"/>
      </svg>
      <span>www.restfulchairdental.example</span>
    </div>
  </section>

  <!-- Front cover panel -->
  <section class="panel panel-cover">
    <svg class="panel-art" viewBox="0 0 380 760">
      <defs>
        <linearGradient id="portrait-photo" x1="0" y1="0" x2="1" y2="1">
          <stop offset="0" stop-color="var(--photo-warm)"/>
          <stop offset=".5" stop-color="#d8d8d8"/>
          <stop offset="1" stop-color="var(--photo-cool)"/>
        </linearGradient>
      </defs>
      <path d="M0,150 Q200,100 380,80 L380,560 Q200,600 0,640 Z" fill="url(#portrait-photo)" role="img" aria-label="Portrait of Dr. Marlon Quade in navy scrubs with a stethoscope"/>
      <path d="M130,140 Q260,90 380,70 L380,130 Q300,100 250,125 Z" fill="var(--heading-blue)"/>
      <path d="M0,150 Q200,100 380,80" fill="none" stroke="var(--brand-green)" stroke-width="10"/>
      <path d="M0,665 Q220,620 380,520 L380,760 L0,760Z" fill="var(--brand-blue)"/>
      <path d="M0,650 Q220,605 380,505" fill="none" stroke="var(--brand-green)" stroke-width="12"/>
      <path d="M0,664 Q220,619 380,519" fill="none" stroke="#fff" stroke-width="6"/>
    </svg>
    <h1 class="cover-title">Sleep <span class="accent">Dentistry</span></h1>
    <div class="meet-block">
      <p class="meet-word">MEET</p>
      <p class="meet-name">DR. ROWAN ELKE MARLON QUADE ,DDS</p>
    </div>
  </section>

</main>
</body>
</html>
```